Beauty Page

**UPDATED Brief**
We are looking for a website for a beauty organisation that targets both MEN & WOMAN. The focus of the company is in four main areas:

- Health
* Naturopathy & Remedial Massage
- Body
* Yoga
* Personal Training
* Massage
- Skin
* Skin care products such as Velquessa
- Beauty
* Waxing
* Eye Treatments

We have attached the logo, (a sample of the website that I did - based on the book) and the sample of the pdf book
Updates

Dear All,

Thank you for your patience regarding the beauty contest. We were not happy with the designs that were submitted to us. We therefore had the Graphic designer to do the pricelist book to get all the colours for the organisation.

We are now happy to relaunch the contest and invite you all to take a look at the brief, download a sample of the book and the website we designed on what I’m looking for (the website is only a draft so I don’t want you to copy it) and let your creative mind go wild and present some suggestions to us.

Thanks

 

Target Market(s)

Woman & Men age 24 - 60

Industry/Entity Type

It Company

Requirements
Must have
• Use of main colours
Black
White
Gray - (CYMK - 65, 58, 57, 37)
Purpleish - Maroon (CYMK - 52, 69, 47, 25)

Use of the three color dots on the page.
(white, maroon & Gray)
Same fonts as the book
- Helvetica LT Std
Should not have
• Logo must not be altered i.e different colours, fonts, shadows etc...

```html
<!DOCTYPE html>
<html lang="en">
<head>
<meta charset="utf-8">
<title>Kalora and Beauty</title>
<link rel="stylesheet" href="https://fonts.googleapis.com/css2?family=Arimo:ital,wght@0,400;0,700;1,400;1,700&family=Didact+Gothic&display=swap">
<style>
:root{
  --white:#ffffff;
  --black:#0b0b0b;
  --ink:#1a1a1a;
  --grey:#384345;
  --grey-mid:#6b7476;
  --grey-light:#dfe1e2;
  --maroon:#5c3b65;
  --maroon-dark:#432a4a;
  --page:#e6e7e9;
  --card:#f3f3f5;
  --footer-text:#c8c8c8;
  --bar:#2b2b2b;
}
*{box-sizing:border-box;margin:0;padding:0}
html,body{width:1200px;height:1128px;overflow:hidden}
body{position:relative;background:var(--page);font-family:"Arimo",Arial,sans-serif;color:var(--ink)}
.abs{position:absolute}
.hero{left:0;top:0;width:1200px;height:443px;background:linear-gradient(160deg,#fafafa 0%,#eeeff0 35%,#d9dcdd 75%,#c9cdce 100%)}
.hero-wave{left:0;top:0}
.hero-photo{left:646px;top:47px;width:447px;height:396px;background:radial-gradient(ellipse at 55% 45%,#f2d7c6 0%,#e9c4ad 35%,rgba(215,218,220,0) 72%)}
.util-bar{left:663px;top:0;width:382px;height:28px;background:linear-gradient(#3a3a3a,#111);border-radius:0 0 4px 4px;color:#eee;font-size:11px;display:flex;align-items:center;justify-content:space-around;padding:0 6px}
.logo{left:163px;top:18px;font-weight:700;font-size:44px;color:var(--grey);letter-spacing:-1px;line-height:1}
.logo small{display:block;font-size:44px;margin-left:52px}
.tagline{left:163px;top:202px;font-style:italic;font-weight:700;font-size:23px;color:var(--black)}
.contact{left:163px;top:234px;font-style:italic;font-weight:700;font-size:21px;color:var(--maroon)}
.dots{left:163px;top:269px;display:flex;gap:7px}
.dots span{width:10px;height:10px;border-radius:50%;border:1px solid var(--grey-mid)}
.intro{left:163px;top:284px;width:525px;font-family:"Didact Gothic",sans-serif;font-size:17px;line-height:20.5px;color:#222}
.pager{left:163px;top:389px;display:flex;gap:3px}
.pager span{width:28px;height:28px;border:1px solid var(--grey);border-radius:3px;background:linear-gradient(#9aa2a4,var(--grey-mid));color:#fff;font-family:"Didact Gothic",sans-serif;font-size:17px;display:flex;align-items:center;justify-content:center}
.pager span.active{background:linear-gradient(var(--maroon),var(--maroon-dark));border-color:var(--maroon-dark)}
.nav{left:0;top:443px;width:1200px;height:42px;background:linear-gradient(var(--maroon) 0,var(--maroon) 3px,#56605f 4px,var(--grey) 100%);border-bottom:3px solid var(--black)}
.nav a{position:absolute;top:9px;color:#fff;text-decoration:none;font-family:"Didact Gothic",sans-serif;font-size:18px}
.nav i{position:absolute;top:3px;width:1px;height:39px;background:#222;border-right:1px solid #6f7a7b}
.card{background:linear-gradient(#fafafc,var(--card));border:1px solid #fff;overflow:hidden}
.card h2{position:absolute;left:11px;top:8px;font-family:"Didact Gothic",sans-serif;font-weight:400;font-size:26px;color:var(--ink)}
.card h2 em{font-style:normal;color:var(--maroon)}
.more{position:absolute;right:6px;bottom:4px;font-size:12px;color:#222}
.ph{position:absolute}
.treat-text{position:absolute;left:12px;top:58px;width:205px;font-style:italic;font-size:13px;line-height:16.5px;color:#222;z-index:1}
.quote{position:absolute;left:22px;top:55px;width:185px;font-size:11.5px;line-height:14px;color:#333}
.news{position:absolute;left:33px;width:262px;font-size:11.5px;line-height:14px;color:#333}
.news em{font-style:normal;color:var(--maroon)}
.rule{position:absolute;left:12px;width:288px;border-top:1px dotted #555}
.video{background:#000;color:#fff;border-radius:0 5px 0 0}
.video p{position:absolute;left:0;top:40px;width:100%;text-align:center;font-style:italic;font-weight:700;font-size:13px;line-height:17px}
.controls{position:absolute;left:0;bottom:0;width:100%;height:16px;background:linear-gradient(#eee,#bbb);font-size:8px;font-weight:700;color:#111}
.footer-top{left:0;top:929px;width:1200px;height:5px;background:repeating-linear-gradient(90deg,#777 0 3px,#aaa 3px 5px)}
.footer{left:0;top:934px;width:1200px;height:152px;background:linear-gradient(#1b1b1b,#050505)}
.links{position:absolute;top:20px;list-style:none}
.links li{font-size:12px;color:var(--footer-text);height:19px;letter-spacing:.3px;white-space:nowrap}
.links li::before{content:"\203A";font-weight:700;font-size:16px;color:#fff;display:inline-block;width:18px;line-height:12px}
.vdiv{position:absolute;top:24px;height:112px;border-left:1px dashed #aaa}
.news-title{position:absolute;left:870px;top:20px;color:#fff;font-style:italic;font-size:21px;letter-spacing:-.5px}
.news-sub{position:absolute;left:870px;top:48px;width:200px;color:#ddd;font-size:10.5px;line-height:13px}
.signup{position:absolute;left:870px;top:92px;width:210px;height:31px;border:1px solid #fff;border-radius:4px;background:#1c1c1c;color:#ddd;font-size:12.5px;padding:8px 7px}
.signup span{position:absolute;right:0;top:0;width:42px;height:29px;background:#f2f2f2;border-radius:0 3px 3px 0}
.bottom{left:0;top:1091px;width:1200px;height:37px;background:var(--bar);border-top:2px solid #888;color:#eee;font-size:13.5px}
.social{position:absolute;top:6px;width:26px;height:26px;border-radius:4px}
</style>
</head>
<body>
<div class="abs hero">
  <svg class="abs hero-wave" width="1200" height="443" aria-hidden="true">
    <path d="M0 140 C300 60 600 300 1200 120" stroke="#ffffff" stroke-opacity=".55" stroke-width="40" fill="none"/>
    <path d="M0 230 C350 120 650 340 1200 200" stroke="#ffffff" stroke-opacity=".4" stroke-width="18" fill="none"/>
  </svg>
  <div class="abs hero-photo" role="img" aria-label="Portrait photo of a woman with clear skin touching her face"></div>
</div>
<div class="abs util-bar"><span>Your Cart is Empty: AUD</span><span>|</span><span>&#9656; Checkout Now</span><span>|</span><span>My Account &#9662;</span></div>
<div class="abs logo">Kalora<small>and Beauty</small></div>
<h1 class="abs tagline">Health, Body &amp; Skin Care Centre</h1>
<div class="abs contact">Contact Us: (08) 5550 1427</div>
<div class="abs dots" aria-hidden="true"><span style="background:var(--white)"></span><span style="background:var(--maroon)"></span><span style="background:var(--grey)"></span></div>
<p class="abs intro">Kalora &amp; Beauty is a health, massage skincare centre that provides quality treatments and education to each and every client to cater for all individuals.</p>
<div class="abs pager"><span class="active">1</span><span>2</span><span>3</span><span>4</span></div>

<nav class="abs nav">
  <a style="left:164px">Home</a><i style="left:263px"></i>
  <a style="left:314px">About Us</a><i style="left:438px"></i>
  <a style="left:490px">Services &amp; Treatments</a><i style="left:731px"></i>
  <a style="left:779px">Contact Us</a>
</nav>

<section class="abs card" style="left:163px;top:514px;width:304px;height:159px">
  <h2>Latest <em>Products</em></h2>
  <div class="ph" style="left:38px;top:40px;width:216px;height:112px;background:radial-gradient(ellipse,#dfe2ea 0%,rgba(230,230,236,0) 70%)" role="img" aria-label="Marea Skin cream tubes and jars"></div>
  <div class="ph" style="left:195px;top:30px;width:90px;height:40px;background:var(--maroon);transform:rotate(32deg);border-radius:4px" role="img" aria-label="Ribbon inviting visitors to explore the Marea Skin range"></div>
  <span class="more">Click here &raquo;</span>
</section>
<section class="abs card" style="left:467px;top:514px;width:310px;height:159px">
  <div class="ph" style="left:0;top:0;width:310px;height:159px;background:linear-gradient(90deg,#f6f4f4 0%,#eee2dc 55%,#d9b7a8 100%)" role="img" aria-label="Woman relaxing during a spa treatment with flowers"></div>
  <h2>Treatments</h2>
  <p class="treat-text">Kalora &amp; Beauty only use the highest quality wax. Hot wax and strip wax is available and we do not recycle our wax.</p>
  <span class="more" style="color:#fff">Click here &raquo;</span>
</section>
<section class="abs card" style="left:777px;top:514px;width:303px;height:159px;border-radius:0 5px 0 0">
  <div class="ph" style="left:215px;top:12px;width:88px;height:147px;background:radial-gradient(ellipse at 50% 45%,#f3d3b4 0%,#f0c987 40%,rgba(240,240,240,0) 75%)" role="img" aria-label="Smiling client photo"></div>
  <h2>Real <em>Stories</em></h2>
  <span style="position:absolute;left:14px;top:42px;font-size:20px">&ldquo;</span>
  <p class="quote">It is a long established fact that a reader will be distracted by the readable content of a page when looking at its layout.</p>
  <span style="position:absolute;left:129px;top:120px;font-family:'Didact Gothic',sans-serif;font-size:14px">Tamsin &nbsp;&nbsp;&nbsp;&rdquo;</span>
  <span class="more" style="left:9px;right:auto">Click here &raquo;</span>
</section>

<section class="abs card" style="left:163px;top:693px;width:304px;height:206px">
  <h2>Latest <em>News</em></h2>
  <p class="news" style="top:48px"><em>It is a long</em> established fact that a reader will be distracted by the readable content of a......</p>
  <div class="rule" style="top:84px"></div>
  <p class="news" style="top:96px"><em>It is a long</em> established fact that a reader will be distracted by the readable content of a......</p>
  <div class="rule" style="top:134px"></div>
  <p class="news" style="top:147px;left:31px"><em>It is a long</em> established fact that a reader will be distracted by the readable content of a......</p>
  <span class="more">Click here &raquo;</span>
</section>
<section class="abs card" style="left:467px;top:693px;width:310px;height:206px">
  <h2>What&rsquo;s <em>New</em></h2>
  <div class="ph" style="left:68px;top:44px;width:190px;height:150px;background:radial-gradient(ellipse,#e6e8ea 0%,#dcdfe1 45%,rgba(240,240,244,0) 75%)" role="img" aria-label="Velquessa skincare bottles"></div>
  <span class="more">Click here &raquo;</span>
</section>
<section class="abs card video" style="left:777px;top:693px;width:303px;height:206px">
  <p>SREVOLUTIONARY NEW<br>TREATMENT VIDEOS</p>
  <svg style="position:absolute;left:140px;top:85px" width="18" height="18" aria-hidden="true"><path d="M2 1 L17 9 L2 17Z" fill="#fff"/></svg>
  <div class="controls">
    <span style="position:absolute;left:6px;top:3px">&#9654;</span>
    <span style="position:absolute;left:22px;top:3px">00:01</span>
    <span style="position:absolute;left:58px;top:6px;width:160px;height:3px;background:#777"></span>
    <span style="position:absolute;left:228px;top:3px">100 %</span>
    <span style="position:absolute;left:272px;top:3px">&#9638;</span>
  </div>
</section>

<div class="abs footer-top"></div>
<footer class="abs footer">
  <ul class="links" style="left:163px"><li>It is a long established</li><li>fact that a reader</li><li>the readable content</li><li>page when looking</li><li>It is a long established</li><li>fact that a reader</li></ul>
  <span class="vdiv" style="left:352px"></span>
  <ul class="links" style="left:380px"><li>It is a long established</li><li>fact that a reader</li><li>the readable content</li><li>page when looking</li><li>It is a long established</li><li>fact that a reader</li></ul>
  <span class="vdiv" style="left:566px"></span>
  <ul class="links" style="left:594px"><li>It is a long established</li><li>fact that a reader</li><li>the readable content</li><li>page when looking</li><li>It is a long established</li><li>fact that a reader</li></ul>
  <span class="vdiv" style="left:785px"></span>
  <div class="news-title">NEWSLETTER</div>
  <p class="news-sub">It is a long established fact that a reader will be distracted</p>
  <div class="signup">E-mail Address<span><svg width="42" height="29" aria-hidden="true"><path d="M16 8 L24 14.5 L16 21" stroke="#111" stroke-width="4" fill="none"/></svg></span></div>
</footer>
<div class="abs bottom">
  <span style="position:absolute;left:160px;top:9px">Copyright &copy; 2011 Kalora&amp;Beauty</span>
  <span style="position:absolute;left:895px;top:9px">Follow us on:</span>
  <span class="social" style="left:983px;background:var(--white)" role="img" aria-label="Social link"></span>
  <span class="social" style="left:1017px;background:var(--maroon)" role="img" aria-label="Feed link"></span>
  <span class="social" style="left:1053px;background:var(--grey-mid)" role="img" aria-label="Social link"></span>
</div>
</body>
</html>
```